Exciting new aperitif brand needs a great label

Vel-Orin is a wonderful rich new premium-priced bitter aperitif, with a deep red colour, from a 100+ year old distillery (1890) near Turin in the Piedmont region of Italy. Inspired by Torvesi, it is perfectly formulated to elevate the classic Baldetti cocktail (and variations on it). It also goes perfectly in a Spritz or a long mixed drink with soda or tonic. The name Vel-Orin is derived from the French for 'peak' and the Italian word for 'love'.

The label, which should take inspiration from Torvesi, but be distinctively different, can incoporate any number of premium label embellishments (foil, embossing, textures etc) and should be no greater than 11cm (height) x 9cm (width) with any core imagery restricted to a width of c.7cm.

The attached mood board should act as inspiration and colour should largely be restricted to reds, blues, whites and perhaps orange. For completeness, the label should note that the ABV is 25% and the bottle size 70cl.

Target Market(s)

21-45yr olds - equal split female/male

Colors
0054AA
0677BA
7BADD7
CADEEF
E8F1F8
0094D4
00A9DD
6FCCEA
C7EBF8
E9F6FB
EE7325
F08F49
F5BC92
FAE3D3
FDF4ED
EB3D1F
EC4F4E
F09395
F8D3D4
FCEDEE

Requirements
Must have
• Great lettering design on the name Vel-Orin

```html
<!DOCTYPE html>
<html lang="en">
<head>
<meta charset="utf-8">
<title>Vel-Orin Aperitivo Label</title>
<link rel="stylesheet" href="https://fonts.googleapis.com/css2?family=EB+Garamond:ital,wght@0,500;0,600;0,700;1,500&family=Pinyon+Script&display=swap">
<style>
  :root {
    --page: #ffffff;
    --page-edge: #9a9a9a;
    --royal-blue: #0a1fc4;
    --navy: #0a1a8a;
    --gold: #c89a4a;
    --gold-dark: #8a6428;
    --cream: #f3e6e4;
    --label-red: #ff0000;
    --ink: #111111;
    --white: #ffffff;
    --leaf-green: #2f9a3a;
    --flower-red: #b0161c;
  }
  html, body {
    margin: 0;
    padding: 0;
    width: 1005px;
    height: 1200px;
    overflow: hidden;
    background: var(--page);
  }
  .canvas {
    position: relative;
    width: 1005px;
    height: 1200px;
    box-sizing: border-box;
    border: 1px solid var(--page-edge);
  }
  .label {
    position: absolute;
    inset: 0;
  }
  .script { font-family: "Pinyon Script", cursive; }
  .serif { font-family: "EB Garamond", serif; }
</style>
</head>
<body>
<main class="canvas">
  <svg class="label" width="1005" height="1200" viewBox="0 0 1005 1200" xmlns="http://www.w3.org/2000/svg">
    <defs>
      <radialGradient id="blue-field" cx="50%" cy="50%" r="70%">
        <stop offset="0" stop-color="#06126a"/>
        <stop offset="1" stop-color="#0a22d0"/>
      </radialGradient>
      <linearGradient id="floral-tone" x1="0" y1="0" x2="1" y2="1">
        <stop offset="0" stop-color="#c7e3c5"/>
        <stop offset="0.5" stop-color="#e9c9c2"/>
        <stop offset="1" stop-color="#dcc79e"/>
      </linearGradient>
      <path id="badge-arc" d="M 432 612 A 95 60 0 0 0 604 612"/>
    </defs>

    <!-- blue field -->
    <rect class="label-field" x="144" y="158" width="742" height="905" fill="url(#blue-field)"/>

    <!-- gold frame with pattern band -->
    <rect class="frame-outer" x="177" y="190" width="677" height="841" fill="none" stroke="var(--gold)" stroke-width="3"/>
    <path class="frame-pattern" role="img" aria-label="Gold and navy geometric border pattern"
          fill="#8f7a4a" fill-rule="evenodd"
          d="M183 196 H848 V1025 H183 Z M218 230 H813 V991 H218 Z"/>
    <rect class="frame-inner" x="219" y="231" width="593" height="759" fill="none" stroke="var(--gold)" stroke-width="3"/>
    <rect class="frame-inner-blue" x="222" y="234" width="587" height="753" fill="var(--royal-blue)"/>

    <!-- cream panel -->
    <rect class="panel" x="226" y="238" width="579" height="745" fill="var(--cream)"/>

    <!-- region flag -->
    <rect class="flag" role="img" aria-label="Red regional flag with white cross" x="463" y="259" width="104" height="68" fill="#e8262b" stroke="#1a2ac0" stroke-width="3"/>

    <!-- top ornaments -->
    <rect role="img" aria-label="Decorative figure among leaves and flowers" x="234" y="262" width="88" height="156" rx="10" fill="url(#floral-tone)"/>
    <rect role="img" aria-label="Decorative figure among leaves and flowers" x="710" y="262" width="88" height="156" rx="10" fill="url(#floral-tone)"/>
    <rect role="img" aria-label="Floral vine ornament" x="326" y="262" width="128" height="64" rx="10" fill="url(#floral-tone)"/>
    <rect role="img" aria-label="Floral vine ornament" x="576" y="262" width="128" height="64" rx="10" fill="url(#floral-tone)"/>

    <!-- region name -->
    <text class="region script" x="461" y="422" text-anchor="middle" font-size="74" fill="var(--gold-dark)" textLength="280" lengthAdjust="spacingAndGlyphs">Piedmont</text>

    <!-- since badge -->
    <ellipse class="badge" cx="517" cy="592" rx="114" ry="74" fill="var(--gold)" stroke="var(--ink)" stroke-width="2"/>
    <ellipse cx="517" cy="590" rx="106" ry="66" fill="var(--label-red)"/>
    <text class="since serif" font-size="20" fill="var(--white)" letter-spacing="7" font-weight="600">
      <textPath href="#badge-arc" startOffset="50%" text-anchor="middle">Since 1890</textPath>
    </text>

    <!-- name banner -->
    <rect class="banner-frame" x="162" y="435" width="706" height="173" fill="var(--gold)" stroke="var(--ink)" stroke-width="3"/>
    <rect class="banner" x="173" y="446" width="684" height="151" fill="var(--label-red)" stroke="var(--ink)" stroke-width="2"/>
    <text class="brand-shadow serif" x="520" y="566" text-anchor="middle" font-size="128" font-weight="600" fill="var(--gold)" stroke="var(--ink)" stroke-width="1" textLength="640" lengthAdjust="spacingAndGlyphs">VEL-ORIN</text>
    <text class="brand serif" x="516" y="562" text-anchor="middle" font-size="128" font-weight="600" fill="var(--white)" stroke="var(--ink)" stroke-width="1.2" textLength="640" lengthAdjust="spacingAndGlyphs">VEL-ORIN</text>

    <!-- mid and lower ornaments -->
    <rect role="img" aria-label="Floral scroll ornament" x="234" y="612" width="150" height="146" rx="12" fill="url(#floral-tone)"/>
    <rect role="img" aria-label="Floral scroll ornament" x="648" y="612" width="150" height="146" rx="12" fill="url(#floral-tone)"/>
    <rect role="img" aria-label="Floral scroll ornament" x="234" y="826" width="150" height="148" rx="12" fill="url(#floral-tone)"/>
    <rect role="img" aria-label="Floral scroll ornament" x="648" y="826" width="150" height="148" rx="12" fill="url(#floral-tone)"/>

    <!-- product type -->
    <text class="type-shadow script" x="523" y="812" text-anchor="middle" font-size="112" fill="var(--gold)" textLength="430" lengthAdjust="spacingAndGlyphs">Aperitivo</text>
    <text class="type script" x="520" y="809" text-anchor="middle" font-size="112" fill="var(--ink)" textLength="430" lengthAdjust="spacingAndGlyphs">Aperitivo</text>
    <text class="tagline script" x="602" y="830" text-anchor="middle" font-size="26" fill="var(--ink)" transform="rotate(-11 602 830)">premium-priced bitter</text>

    <!-- volume -->
    <text class="volume serif" x="516" y="932" text-anchor="middle" font-size="24" font-weight="500" fill="var(--ink)">25% vol. 700 ml.</text>
    <text class="origin serif" x="516" y="960" text-anchor="middle" font-size="15" font-weight="500" fill="var(--ink)" letter-spacing="3.5">PRODUCED BY ITALY</text>
  </svg>
</main>
</body>
</html>
```